Artisan Bread Company needs a business card

I need a business card design, for an artisan bread company called "Hollin's Bread".

I would like the logo on one side, and on the other, I would like it to say

Tavish Hollin
Baker
519.362.4175
hollinsbread@mailvexo.com

Not necessarily in that order- but it must have these.

Industry/Entity Type

Business

Font styles to use
Serif

Requirements
Must have
• The provided logo on the front, this on the back-
• Tavish Hollin
• Baker
• 519.362.4175
• hollinsbread@mailvexo.com

```html
<!DOCTYPE html>
<html lang="en">
<head>
<meta charset="utf-8">
<title>Hollin's Bread – Business Card</title>
<link rel="stylesheet" href="https://fonts.googleapis.com/css2?family=Montserrat:wght@300;400;700;800&display=swap">
<style>
  :root {
    --page-bg: #e9e6e2;
    --card-dark: #2b2b2b;
    --card-dark-deep: #161616;
    --card-mid: #4a4a4a;
    --card-light: #6f6f6f;
    --band-white: #ffffff;
    --ink: #111111;
    --ink-soft: #3a3a3a;
    --rule: #4d4d4d;
    --logo-ink: #ffffff;
  }
  * { box-sizing: border-box; margin: 0; padding: 0; }
  html, body {
    width: 1200px; height: 913px; overflow: hidden;
    background: var(--page-bg);
    font-family: "Montserrat", Arial, sans-serif;
  }
  .canvas { position: relative; width: 1200px; height: 913px; }

  .card {
    position: absolute;
    width: 525px; height: 300px;
    overflow: hidden;
    border-radius: 2px;
    box-shadow: 0 10px 24px rgba(0,0,0,0.22);
    background: linear-gradient(135deg, var(--card-dark-deep) 0%, var(--card-dark) 45%, var(--card-light) 100%);
  }
  .card--front { left: 110px; top: 110px; }
  .card--back  { left: 565px; top: 500px; }

  .card__shapes { position: absolute; inset: 0; width: 100%; height: 100%; }

  .logo {
    position: absolute;
    display: flex; align-items: center; gap: 10px;
    color: var(--logo-ink);
    font-weight: 300;
    white-space: nowrap;
  }
  .logo__dot {
    width: 10px; height: 10px; border-radius: 50%;
    background: var(--logo-ink);
  }
  .card--front .logo { left: 150px; top: 92px; width: 290px; justify-content: center; font-size: 34px; }
  .card--back  .logo { left: 28px; top: 62px; width: 240px; justify-content: center; font-size: 26px; }

  .identity {
    position: absolute; left: 28px; top: 218px;
    color: var(--ink);
  }
  .identity__name { font-size: 22px; letter-spacing: 0.5px; white-space: nowrap; }
  .identity__first { font-weight: 800; }
  .identity__last { font-weight: 300; }
  .identity__role {
    font-size: 10px; font-weight: 700; letter-spacing: 1px;
    text-align: right; margin-top: 2px;
  }

  .contact {
    position: absolute; left: 318px; top: 190px;
    border-left: 1px solid var(--rule);
    padding-left: 16px; height: 72px;
    display: flex; flex-direction: column; justify-content: center; gap: 12px;
    color: var(--ink-soft);
    font-size: 11px; font-weight: 400;
  }
  .contact__item { display: flex; align-items: center; gap: 9px; white-space: nowrap; }
  .contact__icon { width: 13px; height: 13px; flex: none; }
</style>
</head>
<body>
<main class="canvas">

  <!-- Front: brand side -->
  <section class="card card--front" aria-label="Business card front">
    <svg class="card__shapes" viewBox="0 0 525 300" aria-hidden="true">
      <defs>
        <linearGradient id="frontPanel" x1="0" y1="0" x2="1" y2="1">
          <stop offset="0" stop-color="#1c1c1c"/>
          <stop offset="1" stop-color="#3a3a3a"/>
        </linearGradient>
      </defs>
      <polygon points="340,0 525,0 525,205 470,205" fill="#ffffff" opacity="0.07"/>
      <rect x="150" y="40" width="290" height="165" fill="url(#frontPanel)"/>
      <polygon points="0,300 0,205 300,205 308,196 346,196 354,205 525,205 525,300" fill="var(--band-white)"/>
    </svg>
    <div class="logo"><span class="logo__dot"></span>Hollin's Bread</div>
  </section>

  <!-- Back: contact side -->
  <section class="card card--back" aria-label="Business card back">
    <svg class="card__shapes" viewBox="0 0 525 300" aria-hidden="true">
      <defs>
        <linearGradient id="backPanel" x1="0" y1="0" x2="1" y2="1">
          <stop offset="0" stop-color="#141414"/>
          <stop offset="1" stop-color="#333333"/>
        </linearGradient>
      </defs>
      <rect x="0" y="30" width="290" height="150" fill="url(#backPanel)"/>
      <rect x="0" y="180" width="525" height="120" fill="var(--band-white)"/>
      <line x1="318" y1="186" x2="505" y2="186" stroke="var(--rule)" stroke-width="1"/>
    </svg>
    <div class="logo"><span class="logo__dot"></span>Hollin's Bread</div>

    <div class="identity">
      <p class="identity__name"><span class="identity__first">TAVISH</span> <span class="identity__last">HOLLIN</span></p>
      <p class="identity__role">BAKER</p>
    </div>

    <div class="contact">
      <p class="contact__item">
        <svg class="contact__icon" viewBox="0 0 24 24" aria-hidden="true"><path fill="#333" d="M6.6 10.8a15.1 15.1 0 0 0 6.6 6.6l2.2-2.2c.3-.3.7-.4 1-.2 1.1.4 2.3.6 3.6.6.6 0 1 .4 1 1V20c0 .6-.4 1-1 1A17 17 0 0 1 3 4c0-.6.4-1 1-1h3.5c.6 0 1 .4 1 1 0 1.3.2 2.5.6 3.6.1.3 0 .7-.2 1z"/></svg>
        519.362.4175
      </p>
      <p class="contact__item">
        <svg class="contact__icon" viewBox="0 0 24 24" aria-hidden="true"><path fill="#333" d="M2 5h20v14H2z"/><path fill="none" stroke="#fff" stroke-width="1.6" d="M2.5 5.5 12 13l9.5-7.5"/></svg>
        hollinsbread@mailvexo.com
      </p>
    </div>
  </section>

</main>
</body>
</html>
```